Weddings by Marla

Nice ad or card design to advertise my hair business. I like to accentuate 'Marla'

some of the things on my card/ad now are:

Full service hair artist
Available for your special occasion

up-do's for you or your sheitle
Temporary hair extensions, cuts, color, Hi-lites, perms, and waxing

phone, emial, website
Updates

Project Deadline Extended
Reason: I chose a design but it needed a minor change but i have not heard back from the designer. I am still hoping to finalize that design. thank you

Target Market(s)

women all ages

Industry/Entity Type

Hair

```html
<!DOCTYPE html>
<html lang="en">
<head>
<meta charset="utf-8">
<title>Weddings by Marla</title>
<link rel="stylesheet" href="https://fonts.googleapis.com/css2?family=Cinzel:wght@400;500;600&family=Great+Vibes&display=swap">
<style>
  :root {
    --cream: #f6f1ea;
    --ivory: #fbf8f3;
    --hair-light: #d6b08c;
    --hair-mid: #c0946f;
    --hair-deep: #a97d5c;
    --column: #eadbcf;
    --white: #ffffff;
    --ink: #111111;
    --slate: #4a4a4a;
  }
  * { margin: 0; padding: 0; box-sizing: border-box; }
  html, body { width: 1200px; height: 900px; overflow: hidden; background: var(--cream); }
  .ad {
    position: relative;
    width: 1200px;
    height: 900px;
    overflow: hidden;
    font-family: "Cinzel", serif;
  }
  .bridal-updo-photo {
    position: absolute;
    inset: 0;
    background:
      radial-gradient(ellipse 330px 560px at 570px 560px, var(--hair-deep) 0%, var(--hair-mid) 45%, var(--hair-light) 75%, rgba(214,176,140,0) 100%),
      linear-gradient(90deg, rgba(234,219,207,0) 0%, rgba(234,219,207,0) 87%, var(--column) 89%, var(--column) 97%, var(--ivory) 98%),
      radial-gradient(ellipse 700px 600px at 560px 520px, #e6cfb8 0%, var(--cream) 70%, var(--ivory) 100%);
  }
  .contact {
    position: absolute;
    top: 24px;
    right: 8px;
    width: 430px;
    text-align: center;
    font-style: normal;
    color: var(--ink);
    font-size: 25px;
    line-height: 38px;
    letter-spacing: 0.3px;
  }
  .contact .phone { font-size: 23px; }
  .title {
    position: absolute;
    width: 1200px;
    text-align: center;
    color: var(--white);
    white-space: nowrap;
  }
  .title-weddings {
    top: 240px;
    left: 10px;
    font-size: 100px;
    font-weight: 400;
    letter-spacing: 2px;
    line-height: 1;
  }
  .title-by {
    top: 352px;
    left: 10px;
    font-size: 62px;
    font-weight: 400;
    line-height: 1;
    z-index: 2;
  }
  .title-name {
    top: 370px;
    left: 20px;
    font-family: "Great Vibes", cursive;
    font-size: 210px;
    line-height: 1;
    z-index: 1;
  }
  .services {
    position: absolute;
    left: 0;
    width: 1200px;
    text-align: center;
    white-space: nowrap;
  }
  .role {
    top: 692px;
    color: var(--ink);
    font-size: 52px;
    font-weight: 500;
    letter-spacing: 1px;
    line-height: 1;
  }
  .licence {
    top: 742px;
    left: -10px;
    color: var(--slate);
    font-size: 40px;
    letter-spacing: 1px;
    line-height: 1;
  }
  .offerings {
    top: 806px;
    color: var(--white);
    font-size: 30px;
    line-height: 38px;
    letter-spacing: 0.3px;
    text-shadow: 0 1px 3px rgba(0,0,0,0.45);
  }
</style>
</head>
<body>
  <main class="ad">
    <div class="bridal-updo-photo" role="img" aria-label="Photo of a bride's golden blonde twisted up-do with a jeweled hair pin, soft bokeh background"></div>

    <address class="contact">
      <p class="email">Marlastyles@example.net</p>
      <p class="web">marlastyleshair.com</p>
      <p class="phone">555.014.2237</p>
    </address>

    <h1>
      <span class="title title-weddings">Weddings</span>
      <span class="title title-name">Marla</span>
      <span class="title title-by">by</span>
    </h1>

    <p class="services role">FULL SERVICE HAIR ARTIST</p>
    <p class="services licence">LICENSED COSMETOLOGIST</p>
    <p class="services offerings">Up-do's (sheitles too), temporary extensions (rent or buy)<br>cuts, color, hi-lites, and waxing</p>
  </main>
</body>
</html>
```